BrightKeel Business Card Contest

We are looking for a modern business card that catches attention and is unique. Attached is the brand guide and logo files. Please note that the back side (not the side with our name and info) with be UV raise printed, so have fun with the design there. We want to include Name, Title, Phone number, email, website.

Contact Information for Business Card

Please see project description

```html
<!DOCTYPE html>
<html lang="en">
<head>
<meta charset="UTF-8">
<title>BrightKeel Business Card</title>
<link href="https://fonts.googleapis.com/css2?family=Montserrat:wght@300;400;500;600;700&display=swap" rel="stylesheet">
<style>
  :root {
    --stage: #31368a;
    --ink: #1f1f26;
    --white: #ffffff;
    --blue-deep: #0a5fc9;
    --blue: #2a9ff0;
    --cyan: #18c6ea;
    --orange: #f07a1e;
    --red: #d9201f;
    --crimson: #c40008;
    --peach: #ffe6c8;
    --mist: #d9e4f2;
    --sky: #8ebce6;
  }
  * { margin: 0; padding: 0; box-sizing: border-box; }
  html, body { width: 1000px; height: 1200px; overflow: hidden; }
  body {
    background: var(--stage);
    font-family: "Montserrat", sans-serif;
    position: relative;
  }
  .card {
    position: absolute;
    left: 70px;
    width: 854px;
    height: 489px;
    border-radius: 54px;
    overflow: hidden;
    box-shadow: 0 18px 40px rgba(15, 18, 60, 0.45);
  }
  .card-front {
    top: 70px;
    background:
      radial-gradient(ellipse 45% 40% at 48% 28%, rgba(255,255,255,1) 0%, rgba(255,255,255,0.9) 40%, rgba(255,255,255,0) 100%),
      radial-gradient(ellipse 45% 55% at 100% 100%, var(--red) 0%, rgba(217,32,31,0.6) 40%, rgba(217,32,31,0) 80%),
      radial-gradient(ellipse 40% 50% at 82% 75%, var(--orange) 0%, rgba(240,122,30,0) 75%),
      radial-gradient(ellipse 45% 55% at 95% 5%, var(--peach) 0%, rgba(255,230,200,0) 80%),
      radial-gradient(ellipse 40% 45% at 58% 95%, var(--cyan) 0%, rgba(24,198,234,0) 80%),
      radial-gradient(ellipse 55% 65% at 0% 100%, var(--blue-deep) 0%, rgba(10,95,201,0.7) 40%, rgba(10,95,201,0) 85%),
      radial-gradient(ellipse 50% 50% at 0% 0%, var(--mist) 0%, rgba(217,228,242,0) 80%),
      linear-gradient(180deg, #ffffff 0%, #9fd6f2 60%, #2aa8e6 100%);
  }
  .card-back {
    top: 612px;
    background:
      radial-gradient(ellipse 30% 30% at 0% 0%, #ffffff 0%, rgba(255,255,255,0) 100%),
      radial-gradient(ellipse 40% 55% at 100% 10%, var(--crimson) 0%, rgba(196,0,8,0.7) 40%, rgba(196,0,8,0) 90%),
      radial-gradient(ellipse 30% 45% at 98% 100%, var(--sky) 0%, rgba(142,188,230,0) 90%),
      radial-gradient(ellipse 30% 45% at 55% 100%, var(--orange) 0%, rgba(240,122,30,0) 90%),
      radial-gradient(ellipse 40% 70% at 0% 75%, var(--cyan) 0%, rgba(24,198,234,0) 90%),
      radial-gradient(ellipse 35% 55% at 45% 0%, #1e86e6 0%, rgba(30,134,230,0) 90%),
      linear-gradient(90deg, #6ee0f8 0%, #3aa6d8 35%, #7a6a8a 65%, #c8282e 100%);
  }
  .brand {
    position: absolute;
    display: flex;
    align-items: center;
    gap: 12px;
    transform: translateX(-50%);
    white-space: nowrap;
  }
  .brand-mark {
    display: block;
    border-radius: 6px;
  }
  .brand-name {
    font-weight: 500;
    letter-spacing: -1px;
    line-height: 1;
  }
  .card-front .brand { left: 434px; top: 88px; }
  .card-front .brand-mark { width: 58px; height: 58px; background: var(--ink); }
  .card-front .brand-name { font-size: 70px; color: var(--ink); }
  .card-back .brand { left: 443px; top: 196px; }
  .card-back .brand-mark { width: 64px; height: 64px; background: var(--white); }
  .card-back .brand-name { font-size: 78px; color: var(--white); }

  .holder {
    position: absolute;
    left: 70px;
    top: 318px;
    color: var(--white);
  }
  .holder-name { font-size: 32px; font-weight: 700; line-height: 1; }
  .holder-title { font-size: 18px; font-weight: 300; margin-top: 10px; letter-spacing: 0.5px; }

  .contacts {
    position: absolute;
    left: 70px;
    top: 410px;
    display: flex;
    align-items: center;
    color: var(--white);
    font-size: 20.5px;
    font-weight: 500;
    list-style: none;
  }
  .contact { display: flex; align-items: center; gap: 13px; }
  .contact + .contact { margin-left: 42px; }
  .contact svg { width: 25px; height: 25px; flex: none; }
</style>
</head>
<body>
  <section class="card card-front">
    <div class="brand">
      <span class="brand-mark"></span>
      <span class="brand-name">BrightKeel</span>
    </div>
    <div class="holder">
      <h1 class="holder-name">John Due</h1>
      <p class="holder-title">Manager</p>
    </div>
    <ul class="contacts">
      <li class="contact">
        <svg viewBox="0 0 24 24" aria-hidden="true"><path fill="#fff" d="M6.6 10.8a15.2 15.2 0 0 0 6.6 6.6l2.2-2.2c.3-.3.7-.4 1-.2 1.1.4 2.3.6 3.6.6.6 0 1 .4 1 1V20c0 .6-.4 1-1 1A17 17 0 0 1 3 4c0-.6.4-1 1-1h3.5c.6 0 1 .4 1 1 0 1.3.2 2.5.6 3.6.1.3 0 .7-.2 1z"/></svg>
        <span>1800 555 014</span>
      </li>
      <li class="contact">
        <svg viewBox="0 0 24 24" aria-hidden="true"><g fill="none" stroke="#fff" stroke-width="2.2"><circle cx="12" cy="12" r="4"/><path d="M16 8v5.5a2.5 2.5 0 0 0 5 0V12a9 9 0 1 0-3.6 7.2"/></g></svg>
        <span>email@website.com</span>
      </li>
      <li class="contact">
        <svg viewBox="0 0 24 24" aria-hidden="true"><g fill="none" stroke="#fff" stroke-width="1.8"><circle cx="12" cy="12" r="10"/><ellipse cx="12" cy="12" rx="4.5" ry="10"/><path d="M2 12h20M4 7h16M4 17h16"/></g></svg>
        <span>www.website.com</span>
      </li>
    </ul>
  </section>

  <section class="card card-back">
    <div class="brand">
      <span class="brand-mark"></span>
      <span class="brand-name">BrightKeel</span>
    </div>
  </section>
</body>
</html>
```